Cosmetic rework of website. Graphic arts only. We have a developer working in html

Our website structure (basic graphics, number of pages and information) is finished and we generally like it. We have a placeholder site built on Wordpress, and a developer coding that site into html.
The contest is for a cosmetic redo of our site. We will give you our new logo design which we want designed in, and two other sites where we like the "look and feel". we would like to adopt some of that without disturbing our information or where it is. We can think of this as a House all built, and we need an interior designer. our developer will code everything. All we need from the contest winner is artistic tasks.

Our site is here: https://velmarkora.com
the sites we like for "look and feel" are...
https://tarnelwick.com
https://mirolundsolvenharvest.com/

Most important is color palette. We had built everything on green as our central logo color, but we made a major decision to change to red/maroon. We now need a overhaul of the color palette of the site

Target Market(s)

Fresh Pet food

Industry/Entity Type

Pet food

Number of Pages Required

5+ page

Colors
EB3D1F
EC4F4E
F09395
F8D3D4
FCEDEE
E54698
E96AAD
F1A4CE
F9D9EA
FCEFF6
A7469A
B969AE
D3A5CF
EDDBEB
F8F0F9
6B429C
8869AF
B7A5CE
E3DAEB
F3F0F8

Requirements
Must have
• good color working off our logo colors
Nice to have
• it is all about the cosmetics. If you see other more structural suggestions, feel free to incorporate, but we are focused on colors and visual appeal
Should not have
• Visual appeal and a satisfying color palette

```html
<!DOCTYPE html>
<html lang="en">
<head>
<meta charset="utf-8">
<title>Contact Us – Velmarkora</title>
<link href="https://fonts.googleapis.com/css2?family=Poppins:wght@400;500;600;700&display=swap" rel="stylesheet">
<style>
:root{
  --red:#c42a1e;
  --red-deep:#a81f16;
  --maroon:#4a140e;
  --maroon-dark:#3a0f0a;
  --yellow:#f8c70c;
  --ink:#2a2a2a;
  --muted:#6d6d6d;
  --white:#ffffff;
  --shadow:0 6px 18px rgba(0,0,0,.12);
}
*{box-sizing:border-box;margin:0;padding:0}
html,body{width:1200px;height:2320px;overflow:hidden}
body{position:relative;font-family:'Poppins',sans-serif;background:var(--white);color:var(--ink)}
.abs{position:absolute}

/* top bar */
.topbar{left:0;top:0;width:1200px;height:30px;background:var(--red);color:var(--white);font-size:11px;display:flex;align-items:center;justify-content:space-between;padding:0 210px 0 400px}
.topbar span{display:flex;align-items:center;gap:6px}
.topbar .right{display:flex;gap:40px}

/* nav */
.nav{left:0;top:30px;width:1200px;height:60px;background:var(--white);display:flex;align-items:center}
.brand{position:absolute;left:210px;top:-2px;display:flex;flex-direction:column;align-items:center}
.brand-dot{width:48px;height:48px;border-radius:50%;background:var(--red);border:3px solid var(--white);box-shadow:var(--shadow)}
.brand-name{font-size:11px;font-weight:700;color:var(--red);letter-spacing:1px;margin-top:1px}
.menu{position:absolute;left:362px;display:flex;gap:26px;font-size:13px;font-weight:500;color:var(--ink)}
.buy{position:absolute;left:904px;top:17px;background:var(--yellow);border-radius:14px;padding:5px 16px;font-size:12px;font-weight:600;color:var(--maroon)}

/* hero */
.hero{left:0;top:90px;width:1200px;height:420px;background:linear-gradient(90deg,#7a2412 0%,#c0501f 35%,#d9893a 55%,#a73c1b 80%,#6e1f10 100%)}
.hero-title{left:0;top:285px;width:1200px;text-align:center;font-size:44px;font-weight:600;color:var(--white)}
.hero-wave{left:0;top:430px}

/* cards */
.card{background:var(--white);border-radius:10px;box-shadow:var(--shadow);border-bottom:5px solid var(--red);display:flex;align-items:center;justify-content:center;font-size:17px;font-weight:600;color:var(--ink)}
.icon{width:58px;height:58px;border-radius:50%;background:var(--red);display:flex;align-items:center;justify-content:center;border:4px solid var(--white);box-shadow:var(--shadow)}

/* write to us */
.write{left:0;top:1240px;width:1200px;height:680px}
.write-title{left:0;top:1300px;width:1200px;text-align:center;font-size:40px;font-weight:600;color:var(--white)}
.field{background:var(--white);border-radius:14px;font-size:12px;color:#9a9a9a;padding:14px 20px}
.submit{left:540px;top:1740px;width:120px;height:42px;border-radius:21px;background:var(--yellow);display:flex;align-items:center;padding-left:20px;font-size:14px;font-weight:600;color:var(--maroon)}
.submit i{position:absolute;right:4px;top:4px;width:34px;height:34px;border-radius:50%;background:var(--maroon)}

/* footer */
.footer{left:0;top:1880px;width:1200px;height:410px}
.f-logo{left:210px;top:1990px;width:70px;height:70px;border-radius:50%;background:var(--red);border:4px solid var(--white)}
.social{top:2078px;width:18px;height:18px;border-radius:50%;background:var(--white)}
.f-col{top:1990px;color:var(--white);font-size:12px;line-height:22px}
.f-col h4{font-size:16px;font-weight:600;margin-bottom:6px}
.f-col p{display:flex;align-items:center;gap:8px}
.news{left:720px;top:2172px;width:186px;height:32px;border-radius:16px;background:var(--white);font-size:11px;color:#9a9a9a;padding:8px 14px}
.news i{position:absolute;right:3px;top:3px;width:26px;height:26px;border-radius:50%;background:var(--red)}
.copy{left:0;top:2290px;width:1200px;height:30px;background:var(--maroon-dark);color:#d9c0bc;font-size:11px;display:flex;align-items:center;padding-left:210px}
</style>
</head>
<body>

<header>
  <div class="abs topbar">
    <span>TOLL FREE: (888) 5 PAW PAL (729-7257)</span>
    <div class="right"><span>info@velmarkora.com</span><span>Log in</span></div>
  </div>
  <nav class="abs nav">
    <div class="brand"><div class="brand-dot"></div><div class="brand-name">VELMARKORA</div></div>
    <div class="menu"><span>Home</span><span>About Us</span><span>Reviews</span><span>FAQs</span><span>A Super Food Revolution</span><span>Contact Us</span></div>
    <div class="buy">Buy Now</div>
  </nav>
</header>

<section>
  <div class="abs hero" role="img" aria-label="Photo of a happy corgi sitting in front of a warm red wall"></div>
  <h1 class="abs hero-title">Contact Us</h1>
  <svg class="abs hero-wave" width="1200" height="90" viewBox="0 0 1200 90"><path d="M0 40 C250 100 450 100 650 60 C850 20 1000 10 1200 30 L1200 90 L0 90Z" fill="#fff"/></svg>
</section>

<section class="contact-cards">
  <div class="abs card" style="left:220px;top:680px;width:370px;height:110px">1-516-555-0148</div>
  <div class="abs card" style="left:610px;top:680px;width:370px;height:110px">info@velmarkora.com</div>
  <div class="abs card" style="left:220px;top:860px;width:760px;height:110px">TOLL FREE: (888) 5 PAW PAL (729-7257)</div>
  <div class="abs card" style="left:220px;top:1040px;width:760px;height:110px">428 Harwell Rd. Lindenport, NY</div>

  <div class="abs icon" style="left:376px;top:640px"><svg width="24" height="24" viewBox="0 0 24 24"><path d="M6.6 10.8a15 15 0 006.6 6.6l2.2-2.2a1 1 0 011-.25 11.4 11.4 0 003.6.57 1 1 0 011 1V20a1 1 0 01-1 1A17 17 0 013 4a1 1 0 011-1h3.5a1 1 0 011 1c0 1.25.2 2.45.57 3.57a1 1 0 01-.25 1z" fill="#fff"/></svg></div>
  <div class="abs icon" style="left:766px;top:640px"><svg width="24" height="24" viewBox="0 0 24 24"><rect x="3" y="5" width="18" height="14" rx="2" fill="#fff"/><path d="M3 7l9 6 9-6" stroke="#c42a1e" stroke-width="2" fill="none"/></svg></div>
  <div class="abs icon" style="left:571px;top:820px"><svg width="24" height="24" viewBox="0 0 24 24"><path d="M6.6 10.8a15 15 0 006.6 6.6l2.2-2.2a1 1 0 011-.25 11.4 11.4 0 003.6.57 1 1 0 011 1V20a1 1 0 01-1 1A17 17 0 013 4a1 1 0 011-1h3.5a1 1 0 011 1c0 1.25.2 2.45.57 3.57a1 1 0 01-.25 1z" fill="#fff"/></svg></div>
  <div class="abs icon" style="left:571px;top:1000px"><svg width="24" height="24" viewBox="0 0 24 24"><path d="M12 2a7 7 0 00-7 7c0 5 7 13 7 13s7-8 7-13a7 7 0 00-7-7zm0 9.5A2.5 2.5 0 1112 6.5a2.5 2.5 0 010 5z" fill="#fff"/></svg></div>
</section>

<section>
  <svg class="abs write" width="1200" height="680" viewBox="0 0 1200 680" role="img" aria-label="Red band with a faint paw print pattern">
    <path d="M0 20 C300 -10 500 50 750 30 C950 10 1100 0 1200 10 L1200 680 L0 680Z" fill="#c42a1e"/>
  </svg>
  <h2 class="abs write-title">Write To Us</h2>
  <div class="abs field" style="left:210px;top:1420px;width:380px;height:48px">Name</div>
  <div class="abs field" style="left:610px;top:1420px;width:380px;height:48px">Email</div>
  <div class="abs field" style="left:210px;top:1500px;width:380px;height:48px">Phone</div>
  <div class="abs field" style="left:610px;top:1500px;width:380px;height:48px">Subject</div>
  <div class="abs field" style="left:210px;top:1580px;width:780px;height:120px">Message</div>
  <div class="abs submit">Submit<i></i></div>
</section>

<footer>
  <svg class="abs footer" width="1200" height="410" viewBox="0 0 1200 410"><path d="M0 40 C300 0 550 60 800 40 C1000 20 1100 10 1200 20 L1200 410 L0 410Z" fill="#4a140e"/></svg>
  <div class="abs f-logo" aria-label="Velmarkora"></div>
  <div class="abs" style="left:206px;top:2066px;color:#fff;font-size:11px;font-weight:700">VELMARKORA</div>
  <div class="abs social" style="left:212px"></div>
  <div class="abs social" style="left:238px"></div>
  <div class="abs social" style="left:264px"></div>

  <div class="abs f-col" style="left:365px">
    <h4>Quick Links</h4>
    <p>Home</p><p>About</p><p>Reviews</p><p>FAQs</p><p>A Superfood Revolution</p><p>Contact Us</p>
  </div>
  <div class="abs f-col" style="left:540px">
    <h4>Useful Links</h4>
    <p>Login</p><p>Sitemap</p><p>Cookie Policy</p><p>Privacy Policy</p><p>Terms &amp; Conditions</p>
  </div>
  <div class="abs f-col" style="left:720px">
    <h4>Contact Us</h4>
    <p>info@velmarkora.com</p><p>428 Harwell Rd. Lindenport, NY</p><p>1-516-555-0148</p><p>Toll Free: (888) 5 PAW PAL (729-7257)</p>
    <h4 style="margin-top:6px">Newsletter</h4>
  </div>
  <div class="abs news">Enter your email<i></i></div>
  <div class="abs copy">© 2021 Velmarkora Inc. All rights reserved.</div>
</footer>

</body>
</html>
```